Business card design needed

We need a business card design for our new company KiraVelle Event Creations, based in Leeton NSW. We will however be serving the whole Riverina area. We plan any events like, Parties, Weddings ext. We would like to see designs that is vibrant but elegant. Mainly we would like to have our Name displayed on the front and all the other info at the back. We need a design that will catch the eye anywhere.Design FRONT AND BACK
Updates

Industry/Entity Type

Events

Contact Information for Business Card

KiraVelle Event Creations
Tessa Verhulst

0461593802
kiravelle@brightmail.example

Believe the Impossible

Requirements
Must have
• Elegant Coulors and Fonts

```html
<!DOCTYPE html>
<html lang="en">
<head>
<meta charset="utf-8">
<title>KiraVelle Event Creations — Business Card</title>
<link rel="stylesheet" href="https://fonts.googleapis.com/css2?family=Josefin+Sans:wght@300&family=EB+Garamond:wght@400&display=swap">
<style>
  :root {
    --backdrop: #f2f2f2;
    --card: #485b53;
    --ink: #d5ddd8;
    --ink-soft: #c3ccc7;
    --flourish: #7a8b83;
    --rule: #5c6e66;
  }
  html, body {
    margin: 0;
    padding: 0;
    width: 1200px;
    height: 741px;
    overflow: hidden;
    background: var(--backdrop);
  }
  .canvas {
    position: relative;
    width: 1200px;
    height: 741px;
  }
  .card {
    position: absolute;
    width: 517px;
    height: 299px;
    background: var(--card);
    box-shadow: 0 1px 3px rgba(0, 0, 0, 0.35);
  }
  .card--front { left: 344px; top: 58px; }
  .card--back  { left: 342px; top: 387px; }

  .flourish {
    position: absolute;
    display: block;
    border-radius: 12px;
    background: linear-gradient(90deg, rgba(122,139,131,0.15), var(--flourish), rgba(122,139,131,0.15));
    opacity: 0.75;
  }
  .card--front .flourish {
    left: 202px; top: 97px;
    width: 111px; height: 17px;
  }
  .brand-name {
    position: absolute;
    left: 0; right: 0;
    top: 127px;
    margin: 0;
    text-align: center;
    font-family: "EB Garamond", serif;
    font-weight: 400;
    font-size: 23px;
    letter-spacing: 0;
    color: var(--ink);
  }

  .card--back .flourish {
    left: 35px; top: 118px;
    width: 192px; height: 28px;
  }
  .person-name {
    position: absolute;
    left: 35px;
    top: 156px;
    margin: 0;
    font-family: "Josefin Sans", sans-serif;
    font-weight: 300;
    font-size: 24px;
    color: var(--ink);
  }
  .name-rule {
    position: absolute;
    left: 35px;
    top: 193px;
    width: 192px;
    height: 1px;
    background: var(--rule);
  }
  .contact {
    position: absolute;
    left: 35px;
    top: 213px;
    margin: 0;
    font-family: "EB Garamond", serif;
    font-size: 14.5px;
    line-height: 19.5px;
    color: var(--ink-soft);
  }
  .contact span { display: block; }
</style>
</head>
<body>
  <main class="canvas">
    <section class="card card--front" aria-label="Card front">
      <div class="flourish" role="img" aria-label="Decorative scroll flourish"></div>
      <h1 class="brand-name">KiraVelle Event Creations</h1>
    </section>

    <section class="card card--back" aria-label="Card back">
      <div class="flourish" role="img" aria-label="Decorative scroll flourish"></div>
      <h2 class="person-name">Tessa Verhulst</h2>
      <div class="name-rule"></div>
      <p class="contact">
        <span class="contact__phone">t: 0461593802</span>
        <span class="contact__email">kiravelle@brightmail.example</span>
      </p>
    </section>
  </main>
</body>
</html>
```